Interior designer needs business card design

I need a card for my new interior design company. I de sign mostly kitchens and baths, but don't want the card to list and specialty. I've gotten several clients already by Dordrecht of mouth, but now need to begin advertising.
I've got a pic of a silk screen used to print my father's old real estate sign and was hoping to use it as the basis for my card design.
Instead of "Sold by Montaldo", I'd like the front of my card to read "Design by Montaldo".
I like the font styles and banner and would like to stay as close to the original as possible, but with some twist--maybe color, not sure. Surprise me!
The back should list my email and phone
montaldodesign@pellomail.com
555-271-0396

```html
<!DOCTYPE html>
<html lang="en">
<head>
<meta charset="utf-8">
<title>Design by Montaldo — Business Cards</title>
<link rel="stylesheet" href="https://fonts.googleapis.com/css2?family=Cinzel:wght@400;700&family=Open+Sans:wght@700&display=swap">
<style>
  :root {
    --bg: #ece7df;
    --card-light: #fbfaf8;
    --card-dark: #4b3b2d;
    --ink: #2b2119;
    --taupe: #a89a87;
    --cream: #f4efe6;
    --shadow: rgba(40, 28, 18, 0.22);
  }
  * { box-sizing: border-box; margin: 0; padding: 0; }
  html, body { width: 1200px; height: 844px; overflow: hidden; }
  body {
    background: var(--bg);
    position: relative;
    font-family: "Cinzel", serif;
    color: var(--ink);
  }
  .card {
    position: absolute;
    width: 340px;
    height: 540px;
    border-radius: 18px;
    box-shadow: 0 10px 24px var(--shadow);
  }
  .card--front {
    left: 170px;
    top: 80px;
    background: var(--card-light);
  }
  .card--back {
    left: 640px;
    top: 170px;
    background: var(--card-dark);
    display: flex;
    align-items: center;
    justify-content: center;
  }
  .brand {
    font-family: "Cinzel", serif;
    font-weight: 700;
    text-align: center;
    line-height: 1.15;
  }
  .card--front .brand {
    position: absolute;
    top: 70px;
    left: 0;
    right: 0;
    font-size: 30px;
    color: var(--ink);
  }
  .card--back .brand {
    font-size: 30px;
    color: var(--cream);
  }
  .contact {
    position: absolute;
    left: 0;
    right: 0;
    top: 300px;
    text-align: center;
  }
  .contact__name {
    font-size: 24px;
    letter-spacing: 1.5px;
    color: var(--ink);
  }
  .contact__phone {
    margin: 12px 0 14px;
    background: var(--ink);
    color: var(--card-light);
    font-family: "Open Sans", sans-serif;
    font-weight: 700;
    font-size: 36px;
    letter-spacing: 1px;
    padding: 4px 0 6px;
  }
  .contact__email {
    font-size: 13px;
    letter-spacing: 0.6px;
    color: var(--ink);
  }
  .mark {
    position: absolute;
    left: 40px;
    top: 700px;
    display: flex;
    align-items: center;
    gap: 16px;
  }
  .mark__square {
    width: 34px;
    height: 34px;
    background: var(--taupe);
  }
  .mark .brand {
    font-size: 32px;
    color: var(--ink);
    text-align: left;
  }
</style>
</head>
<body>
  <section class="card card--front">
    <div class="brand">Design by<br>Montaldo</div>
    <div class="contact">
      <p class="contact__name">Paolo Montaldo</p>
      <p class="contact__phone">555-271-0396</p>
      <p class="contact__email">MONTALDODESIGN@PELLOMAIL.COM</p>
    </div>
  </section>

  <section class="card card--back">
    <div class="brand">Design by<br>Montaldo</div>
  </section>

  <div class="mark">
    <span class="mark__square"></span>
    <div class="brand">Design by Montaldo</div>
  </div>
</body>
</html>
```